Summer Adventure Day - Poster design

Our company is based in the West End of Glasgow. During the summer holidays every weekday we are running a number of Adventure Days for young people aged 8+. The dates are from Monday 2nd July through to Friday 10th August. The activities vary each day but include climbing, hillwalking, bushcraft, kayaking, archery, abseiling and orienteering. The activities run from 8:30am to 4:30pm, and the drop off / pick up location is 14 Marlow Crescent, Ashbrae, Glasgow, G23 4RT.
We are looking for an eye catching poster design that advertises the summer holiday adventure days. We are also needing the poster to be easily adaptable for both our Chatterbook header and to run promotions on Chatterbook. For more information on what we do and for some photos see our chatterbook page - Northgate Trail Collective.

The poster needs to include our logo, the BTVC logo and the PnLT Logo all attached to this brief. The poster needs to direct people to our website to book www.northgatetrailcollective.co.uk
The final design should be bright, colorful, eye catching and make people want to book onto either an adventure day or an adventure week.

The poster should also be easily adaptable to landscape for a billboard as well as portrait for a magazine advert.

Target Market(s)

Parents of children aged 8+

Colors

Designer to choose colors to be used in the design.

Requirements
Must have
• The project must contain our logo, our website address, how to book along with information on what is happening. The poster should also be easily adaptable for both our Chatterbook header and to be able to use for a Chatterbook Advert.
Nice to have
• S0me of the photos from the previous adventure weeks, photos can be found on our chatterbook page - Northgate Trail Collective. Should be bright and colourful and attract more business to our website.
Should not have
• Our mailing address it should be the address for pick up / drop off

```html
<!DOCTYPE html>
<html lang="en">
<head>
<meta charset="utf-8">
<title>Summer Holiday Adventure Days – Poster</title>
<link rel="stylesheet" href="https://fonts.googleapis.com/css2?family=Oswald:wght@500;700&family=Roboto+Condensed:wght@400;700&display=swap">
<style>
  :root {
    --stage: #3b3b3b;
    --ink: #141414;
    --orange: #f07f22;
    --paper: #ffffff;
    --night: #0b0d0c;
  }
  html, body {
    margin: 0;
    padding: 0;
    width: 1200px;
    height: 750px;
    overflow: hidden;
    background: var(--stage);
  }
  .poster {
    position: absolute;
    left: 346px;
    top: 25px;
    width: 507px;
    height: 700px;
    background: var(--paper);
    overflow: hidden;
    font-family: "Roboto Condensed", "Arial Narrow", sans-serif;
  }
  .poster-art {
    position: absolute;
    inset: 0;
    display: block;
  }
  .brand {
    position: absolute;
    top: 58px;
    left: 0;
    right: 0;
    display: flex;
    justify-content: center;
    align-items: center;
    gap: 8px;
  }
  .brand-dot {
    width: 13px;
    height: 13px;
    border-radius: 50%;
    background: var(--orange);
  }
  .brand-name {
    font-family: "Oswald", "Arial Narrow", sans-serif;
    font-weight: 500;
    font-size: 26px;
    color: var(--paper);
    letter-spacing: 0.3px;
  }
  .details {
    position: absolute;
    left: 0;
    right: 0;
    top: 482px;
    text-align: center;
  }
  .headline {
    margin: 0;
    font-family: "Oswald", "Arial Narrow", sans-serif;
    font-weight: 700;
    font-size: 50px;
    line-height: 46px;
    text-transform: uppercase;
    letter-spacing: -0.2px;
  }
  .headline-top { display: block; color: var(--ink); }
  .headline-bottom { display: block; color: var(--orange); }
  .dates {
    margin: 8px 0 0;
    font-size: 12px;
    font-weight: 400;
    color: var(--ink);
  }
  .hours {
    margin: 4px 0 0;
    font-size: 17px;
    line-height: 20px;
    font-weight: 700;
    color: var(--orange);
  }
  .contact {
    margin: 4px 0 0;
    padding: 0;
    list-style: none;
    font-size: 11px;
    line-height: 17px;
    font-weight: 700;
    color: var(--ink);
  }
  .contact li {
    display: flex;
    justify-content: center;
    align-items: center;
    gap: 5px;
  }
  .contact svg { display: block; }
</style>
</head>
<body>
  <main class="poster">
    <svg class="poster-art" viewBox="0 0 507 700" width="507" height="700">
      <defs>
        <linearGradient id="campScene" x1="0" y1="0" x2="0" y2="1">
          <stop offset="0" stop-color="#0b0d0c"/>
          <stop offset="0.2" stop-color="#10201a"/>
          <stop offset="0.4" stop-color="#2c5a44"/>
          <stop offset="0.6" stop-color="#b8345a"/>
          <stop offset="0.78" stop-color="#d8772f"/>
          <stop offset="1" stop-color="#4f7a22"/>
        </linearGradient>
        <radialGradient id="fireGlow" cx="0.36" cy="0.82" r="0.42">
          <stop offset="0" stop-color="#ffb23a" stop-opacity="0.95"/>
          <stop offset="0.5" stop-color="#f07f22" stop-opacity="0.45"/>
          <stop offset="1" stop-color="#f07f22" stop-opacity="0"/>
        </radialGradient>
      </defs>
      <g role="img" aria-label="Photo: group of cheerful children with raised arms sitting around a campfire at dusk, one holding a red guitar, a leader in a red jacket standing behind">
        <rect x="0" y="0" width="507" height="500" fill="url(#campScene)"/>
        <rect x="0" y="0" width="507" height="500" fill="url(#fireGlow)"/>
      </g>
      <polygon class="peak-panel" fill="#ffffff"
        points="0,608 0,483 199,416 223,441 356,354 441,465 507,437 507,700 0,700"/>
      <polyline class="peak-line" fill="none" stroke="#f07f22" stroke-width="5" stroke-linejoin="miter"
        points="0,483 199,416 223,441 356,354 441,465 507,437"/>
    </svg>

    <header class="brand">
      <span class="brand-dot"></span>
      <span class="brand-name">Northgate Trail Collective</span>
    </header>

    <section class="details">
      <h1 class="headline">
        <span class="headline-top">Summer Holiday</span>
        <span class="headline-bottom">Adventure Days</span>
      </h1>
      <p class="dates">Monday 2nd July through to Friday 10th August</p>
      <p class="hours">The activities run from<br>8:30am to 4:30pm,</p>
      <ul class="contact">
        <li>
          <svg width="8" height="10" viewBox="0 0 8 10"><path d="M4 0a4 4 0 0 1 4 4c0 3-4 6-4 6S0 7 0 4a4 4 0 0 1 4-4z" fill="#f07f22"/><circle cx="4" cy="4" r="1.4" fill="#fff"/></svg>
          <span>14 Marlow Crescent, Ashbrae, Glasgow, G23 4RT</span>
        </li>
        <li>
          <svg width="8" height="8" viewBox="0 0 8 8"><circle cx="4" cy="4" r="3.3" fill="none" stroke="#f07f22" stroke-width="1.2"/><path d="M0.8 4h6.4M4 0.8c-1.6 2-1.6 4.4 0 6.4M4 0.8c1.6 2 1.6 4.4 0 6.4" fill="none" stroke="#f07f22" stroke-width="0.8"/></svg>
          <span>www.northgatetrailcollective.co.uk</span>
        </li>
      </ul>
    </section>
  </main>
</body>
</html>
```